Seasons Greetings from Brackfold Hire.

Brackfold Hire is a Temporary Structures company based in South East London (South Bermondsey).
We dry hire Brackfold as well as deliver and manage projects with our own crew.
We are looking for someone to design our Christmas card or as I prefer to say ‘Season’s Greetings Card’ as this includes everyone religious or not.
The card should reflect Brackfold Hire Ltd and what we do, if you take a look at our website please look at the hires section only,
http://www.brackfold.co.uk/stage-hire.htm
Also take a look at our Brackfold Video’s
http://www.vidplume.example/user/firstbrackfold?feature=results_main
We would also like the card to be friendly and humorous,
Card Size: 210mm x 297mm folded to 210mm x 148mm
Suggested text for Front of card: Seasons Greetings from Brackfold Hire
Inner Text has yet to be confirmed but something like: Wishing you a Merry Christmas and a Happy New Year from everyone at Brackfold Hire
A clever use of the Brackfold logo or weave of the deck would be proffered. I have attached a PDF of a previous card.
Please DO Not show the Mantis Risers.
Please let me know if you require anymore info,
Target Market(s)
Brackfold Customers
Industry/Entity Type
Religious
Requirements
Must have
- Must be a professional looking card

```html
<!DOCTYPE html>
<html lang="en">
<head>
<meta charset="utf-8">
<title>Seasons Greetings from Brackfold Hire</title>
<link rel="stylesheet" href="https://fonts.googleapis.com/css2?family=Pinyon+Script&display=swap">
<style>
  :root {
    --paper: #ffffff;
    --cream: #f6f1d6;
    --cream-soft: #fbf8e8;
    --pine: #1f5a26;
    --pine-deep: #123d17;
    --berry: #a8453b;
    --berry-dark: #7e2b24;
  }
  html, body {
    margin: 0;
    padding: 0;
    overflow: hidden;
    background: var(--paper);
  }
  .card {
    position: relative;
    width: 927px;
    height: 1200px;
    overflow: hidden;
    background: var(--paper);
    font-family: "Pinyon Script", cursive;
    color: var(--berry);
  }
  .front-band {
    position: absolute;
    left: 0;
    top: 0;
    width: 927px;
    height: 600px;
    overflow: hidden;
    background: linear-gradient(135deg, var(--cream-soft), var(--paper) 55%, var(--cream-soft));
  }
  .faint-flake {
    position: absolute;
    left: 0;
    top: 0;
    width: 927px;
    height: 600px;
  }
  .green-flake {
    position: absolute;
    left: 447px;
    top: 0;
    width: 480px;
    height: 600px;
    background: radial-gradient(circle at 70% 49%, var(--pine-deep) 0, var(--pine) 30%, rgba(31, 90, 38, 0.55) 55%, rgba(31, 90, 38, 0) 75%);
  }
  .script {
    position: absolute;
    margin: 0;
    font-weight: 400;
    line-height: 1;
    white-space: nowrap;
    color: var(--berry);
  }
  .headline {
    transform-origin: 0 50%;
  }
  .headline-seasons {
    left: 44px;
    top: 140px;
    font-size: 150px;
    transform: rotate(-25deg);
  }
  .headline-greetings {
    left: 142px;
    top: 350px;
    font-size: 120px;
    transform: rotate(-29deg);
  }
  .headline-year {
    left: 240px;
    top: 480px;
    font-size: 120px;
    letter-spacing: 18px;
    transform: rotate(-31deg);
  }
  .wish-line {
    left: 213px;
    top: 690px;
    font-size: 66px;
  }
  .merry-line {
    left: 175px;
    top: 815px;
    font-size: 67px;
  }
  .from-line {
    left: 376px;
    top: 920px;
    font-size: 54px;
  }
  .sign-off {
    position: absolute;
    left: 578px;
    top: 1045px;
    display: flex;
    align-items: center;
    gap: 10px;
    font-family: "Pinyon Script", cursive;
    font-size: 48px;
    line-height: 1;
    color: var(--berry);
  }
  .sign-off .mark {
    width: 14px;
    height: 14px;
    background: var(--berry);
  }
</style>
</head>
<body>
<main class="card">
  <section class="front-band">
    <div class="faint-flake" role="img" aria-label="Large faint cream snowflake decoration behind the greeting"></div>
    <div class="green-flake" role="img" aria-label="Large embossed green snowflake illustration"></div>
    <h1 class="script headline headline-seasons">Seasons</h1>
    <p class="script headline headline-greetings">Greetings</p>
    <p class="script headline headline-year">2012</p>
  </section>

  <section class="inside-message">
    <p class="script wish-line">Wishing you a</p>
    <p class="script merry-line">Merry Christmas</p>
    <p class="script from-line">From you friends at</p>
    <div class="sign-off"><span class="mark"></span><span class="company-name">Brackfold</span></div>
  </section>
</main>
</body>
</html>
```